Brookhaven Commerce Park Media Package

We are looking for a designer to unify our company's image throughout its stationery and marketing deliverables. We will be focusing on:
*Business Cards (3.5 x 2)
*Letter Head (Letter Size)
*PowerPoint Presentation Template,
*One Pager Flyer (Letter Size)
*Front of Elevator's bay: 4 photos of the elevator bays (two groups of 3 elevators) to which we are looking for designs for its doors and surrounding wall (vinyl prints)
*Font's suggestions
*Official color palette.
*Outdoor Street Signage: please use the following dimensions:
Sign #1 (Galloway Side): 48(W)x72"(H) (3 sided)
Sign #2: 24"(W)x48"(H) (3 sided)
Sign #3 (Top of Hill): 30(W)x54(H) (2 sides)
*Carport Sign:
See photos attached. The white letters will be removed, and a new sign will take place. Preferably, Cut-Out fonts, but we can consider an alternative approach for cost effective solution.
Find attached the approved logos.
______________________________________
We are a real estate holding company focused on the commercial office space in the Ohio, US, market.
You can check our site at www.brookhavenpark.example
As inspiration guidelines, we would like to see designs that are modern, minimalistic, dynamic and energetic.
Target Market(s)
General Population, Business Owners, Non-Profit Organizations, Government
Industry/Entity Type
Real Estate - Commercial Office Space - Flex Space

```html
<!DOCTYPE html>
<html lang="en">
<head>
<meta charset="utf-8">
<title>Brookhaven Commerce Park Letterhead</title>
<link rel="stylesheet" href="https://fonts.googleapis.com/css2?family=Montserrat:wght@400;600;700&display=swap">
<style>
  :root {
    --brand-blue: #02408f;
    --brand-navy: #0a1b3d;
    --paper: #ffffff;
    --mark-tint: #e3e8f2;
    --ink: #111111;
  }
  html, body {
    margin: 0;
    padding: 0;
    width: 898px;
    height: 1200px;
    overflow: hidden;
    background: var(--paper);
  }
  .letterhead {
    position: relative;
    width: 898px;
    height: 1200px;
    background: var(--paper);
    font-family: "Montserrat", sans-serif;
    overflow: hidden;
  }
  .letterhead__shapes {
    position: absolute;
    inset: 0;
  }
  .brand {
    position: absolute;
    left: 87px;
    top: 64px;
    display: flex;
    align-items: center;
    gap: 14px;
  }
  .brand__circle {
    width: 96px;
    height: 96px;
    border: 1.5px solid var(--brand-navy);
    border-radius: 50%;
    box-sizing: border-box;
  }
  .brand__name {
    margin: 0;
    font-weight: 700;
    font-size: 30px;
    line-height: 1.05;
    letter-spacing: 0.3px;
    color: var(--ink);
  }
  .brand__sub {
    display: block;
    margin-top: 2px;
    padding-left: 10px;
    font-weight: 400;
    font-size: 17px;
    letter-spacing: 0.2px;
    color: var(--brand-navy);
  }
  .contact {
    position: absolute;
    top: 1037px;
    display: flex;
    align-items: center;
    gap: 10px;
    font-size: 9.5px;
    font-weight: 700;
    color: var(--ink);
  }
  .contact svg {
    width: 29px;
    height: 29px;
  }
  .contact--phone { left: 117px; }
  .contact--email { left: 402px; }
  .contact--location { left: 700px; }
  .website {
    position: absolute;
    left: 0;
    right: 0;
    top: 1163px;
    margin: 0;
    text-align: center;
    color: var(--paper);
    font-weight: 600;
    font-size: 14px;
    letter-spacing: 0.3px;
  }
</style>
</head>
<body>
<main class="letterhead">
  <svg class="letterhead__shapes" width="898" height="1200" viewBox="0 0 898 1200" aria-hidden="true">
    <circle class="background-circle" cx="743" cy="895" r="312" fill="var(--mark-tint)"/>
    <path class="side-band" d="M0 0 L10 0 C40 120 52 230 47 330 C42 480 10 600 12 740 C14 880 25 1000 40 1108 L0 1120 Z" fill="var(--brand-blue)"/>
    <path class="wave-line" d="M40 1108 C130 1090 210 1080 280 1081 C380 1083 480 1100 568 1106" fill="none" stroke="var(--brand-blue)" stroke-width="5" stroke-linecap="round"/>
    <path class="wave-line" d="M635 1106 C730 1104 820 1095 898 1084" fill="none" stroke="var(--brand-blue)" stroke-width="5" stroke-linecap="round"/>
    <path class="footer-band" d="M0 1155 C90 1135 180 1126 260 1128 C400 1132 520 1158 640 1157 C740 1156 820 1145 898 1136 L898 1200 L0 1200 Z" fill="var(--brand-blue)"/>
  </svg>

  <header class="brand">
    <div class="brand__circle"></div>
    <h1 class="brand__name">BROOKHAVEN<span class="brand__sub">Commerce Park</span></h1>
  </header>

  <div class="contact contact--phone">
    <svg viewBox="0 0 30 30"><circle cx="15" cy="15" r="15" fill="var(--brand-blue)"/><path d="M11 8 l3 0 l1 4 l-2 1.5 c1 2.5 2.5 4 5 5 l1.5 -2 l4 1 l0 3 c-7 1 -13 -5 -12.5 -12.5 z" fill="#fff"/></svg>
    <span>555-xxxxxxxx</span>
  </div>
  <div class="contact contact--email">
    <svg viewBox="0 0 30 30"><circle cx="15" cy="15" r="15" fill="var(--brand-blue)"/><rect x="8" y="10" width="14" height="10" rx="1.5" fill="none" stroke="#fff" stroke-width="1.8"/><path d="M8.5 10.5 L15 16 L21.5 10.5" fill="none" stroke="#fff" stroke-width="1.8"/></svg>
    <span>email@domain.com</span>
  </div>
  <div class="contact contact--location">
    <svg viewBox="0 0 30 30"><circle cx="15" cy="15" r="15" fill="var(--brand-blue)"/><path d="M15 7 c-3.6 0 -6 2.6 -6 5.8 c0 4 6 10.2 6 10.2 s6 -6.2 6 -10.2 c0 -3.2 -2.4 -5.8 -6 -5.8 z" fill="#fff"/><circle cx="15" cy="12.8" r="2.2" fill="var(--brand-blue)"/></svg>
    <span>Location</span>
  </div>

  <p class="website">www.brookhavenpark.example</p>
</main>
</body>
</html>
```